Tax Business Advertisement

Pemberly & Associates Tax Services - Need to develop an advertisement tool suitable for print and electronic advertising. My business provides tax preparation and audit representation for Individuals, Partnerships, Corporations, Estates, Trusts and other entities with tax reporting requirements. I recently had business cards designed by your company, design #8270451 and would need the basic information from the business card on the advertisement.

Some of the following wording may be suitable for the advertisement:

Enrolled Agents are licensed to practice by the IRS. Our services include personal and business tax return preparation, tax audits, offers in compromise, back taxes, forming new business, dissolving business, and much more. We are available to provide services in all 50 states.

Enrolled agents are the only federally licensed tax practitioners who specialize in taxation and who have unlimited rights to represent taxpayers before the IRS.

If you are just starting a business, have been in business for a long time, or just an individual who needs a Tax Professional, Pemberly & Associates Tax Services is the right choice for you.

```html
<!DOCTYPE html>
<html lang="en">
<head>
<meta charset="utf-8">
<title>Pemberly &amp; Associates Tax Services</title>
<link rel="stylesheet" href="https://fonts.googleapis.com/css2?family=Gentium+Book+Plus:wght@400;700&family=Playfair+Display:wght@500&family=Oswald:wght@500&display=swap">
<style>
  :root {
    --red: #c9262c;
    --deep-red: #8e1317;
    --ink: #1f1d1e;
    --text: #2a2a2a;
    --paper: #ffffff;
    --photo-light: #dfe6ea;
    --photo-mid: #a8b7c0;
    --portrait: #8a7a70;
  }
  * { margin: 0; padding: 0; box-sizing: border-box; }
  html, body { width: 927px; height: 1200px; overflow: hidden; background: var(--paper); }
  .ad {
    position: relative; width: 927px; height: 1200px; overflow: hidden;
    background: var(--paper); color: var(--text);
    font-family: "Gentium Book Plus", "Palatino Linotype", Georgia, serif;
  }
  .top-swoosh { position: absolute; left: 0; top: 0; }
  .brand {
    position: absolute; left: 418px; top: 72px; display: flex; align-items: flex-start; gap: 18px;
  }
  .brand-square { width: 70px; height: 70px; background: var(--red); margin-top: 2px; }
  .brand-name {
    font-family: "Playfair Display", Georgia, serif; font-weight: 500;
    font-size: 36px; color: var(--ink); line-height: 1; letter-spacing: 0.2px;
    border-bottom: 2px solid var(--red); padding-bottom: 8px;
  }
  .brand-tagline {
    font-family: "Oswald", "Arial Narrow", sans-serif; font-weight: 500;
    font-size: 15px; letter-spacing: 8.6px; color: var(--ink); margin-top: 9px;
  }
  .hero-band { position: absolute; left: 0; top: 186px; width: 927px; height: 12px; background: var(--ink); }
  .hero-photo {
    position: absolute; left: 0; top: 198px; width: 927px; height: 377px;
    background: linear-gradient(110deg, var(--photo-mid) 0%, var(--photo-light) 35%, #f2f3f0 60%, #cfd6c8 100%);
  }
  .hero-rule {
    position: absolute; left: 0; top: 575px; width: 927px; height: 8px;
    background: linear-gradient(90deg, var(--deep-red), var(--red) 50%, var(--deep-red));
  }
  .copy { position: absolute; font-size: 22.5px; line-height: 22px; color: var(--text); }
  .copy-intro { left: 43px; top: 603px; width: 860px; }
  .copy-agents { left: 43px; top: 726px; width: 360px; }
  .copy-choice { left: 43px; top: 895px; width: 380px; }
  .contact-card {
    position: absolute; left: 432px; top: 727px; width: 448px; height: 183px;
    background: var(--red); box-shadow: 4px 4px 0 var(--ink);
  }
  .contact-portrait {
    position: absolute; left: 20px; top: 13px; width: 116px; height: 158px;
    background: linear-gradient(180deg, #ffffff 0%, #ffffff 30%, var(--portrait) 55%, #1d1d1f 100%);
  }
  .contact-details {
    position: absolute; left: 159px; top: 13px; color: var(--paper);
    font-size: 19px; line-height: 26px;
  }
  .contact-heading { font-weight: 700; font-size: 19px; }
  .footer-curve { position: absolute; left: 0; top: 1058px; }
  .footer-url {
    position: absolute; left: 0; top: 1120px; width: 927px; text-align: center;
    color: var(--paper); font-weight: 700; font-size: 31px; letter-spacing: 0.3px;
  }
</style>
</head>
<body>
<div class="ad">
  <svg class="top-swoosh" width="560" height="80" viewBox="0 0 560 80" aria-hidden="true">
    <defs>
      <linearGradient id="swoosh-fill" x1="0" x2="1">
        <stop offset="0" stop-color="#6e0e12"/>
        <stop offset="0.6" stop-color="#c9262c"/>
        <stop offset="1" stop-color="#8e1317"/>
      </linearGradient>
    </defs>
    <path d="M0 0 H545 C400 10 180 30 0 75 Z" fill="url(#swoosh-fill)"/>
    <path d="M0 0 H300 C200 8 90 25 0 50 Z" fill="#1f1d1e" opacity="0.55"/>
  </svg>

  <header class="brand">
    <div class="brand-square"></div>
    <div>
      <div class="brand-name">Pemberly &amp; Associates</div>
      <div class="brand-tagline">TAX AND BUSINESS SERVICES</div>
    </div>
  </header>

  <div class="hero-band"></div>
  <div class="hero-photo" role="img" aria-label="Photo of a tax form, a social security card, reading glasses and a twenty-dollar bill"></div>
  <div class="hero-rule"></div>

  <p class="copy copy-intro">Enrolled Agents are licensed to practice by the IRS. Our services include personal and business tax return preparation, tax audits, offers in compromise, back taxes, forming new business, dissolving business, and much more. We are available to provide services in all 50 states.</p>

  <p class="copy copy-agents">Enrolled agents are the only federally licensed tax practitioners who specialize in taxation and who have unlimited rights to represent taxpayers before the IRS.</p>

  <p class="copy copy-choice">If you are just starting a business, have been in business for a long time, or just an individual who needs a Tax Professional, Pemberly &amp; Associates Tax Services is the right choice for you.</p>

  <aside class="contact-card">
    <div class="contact-portrait" role="img" aria-label="Portrait of the enrolled agent in a dark suit"></div>
    <div class="contact-details">
      <div class="contact-heading">CONTACT US NOW!</div>
      <div>Marcus D. Pemberly III, EA, MS</div>
      <div>P07391528 | (555) 284-6190</div>
      <div>taxdesk411@example.com</div>
      <div>4127 Larkspur Road, Suite D,</div>
      <div>Fair Oaks, CA 95628</div>
    </div>
  </aside>

  <svg class="footer-curve" width="927" height="142" viewBox="0 0 927 142" aria-hidden="true">
    <defs>
      <linearGradient id="footer-red" x1="0" x2="1">
        <stop offset="0" stop-color="#8e1317"/>
        <stop offset="0.5" stop-color="#c9262c"/>
        <stop offset="1" stop-color="#8e1317"/>
      </linearGradient>
    </defs>
    <path d="M0 30 Q463 0 927 30 V142 H0 Z" fill="url(#footer-red)"/>
    <path d="M0 40 Q463 16 927 40 V142 H0 Z" fill="#1f1d1e"/>
  </svg>
  <div class="footer-url">www.pemberlytaxhelp.com</div>
</div>
</body>
</html>
```